KORVa: AI driven decarbonization application

We are seeking an engaging, user-friendly, and visually appealing user interface for our B2B SaaS platform, Brelmont KORVa. This solution helps large organizations achieve net-zero emissions using AI-driven forecasting, AI models, a emission mitigation library, and a scenario simulator..

A big challenge is to allow the user to work efficiently with multidimensional data.

Requirements:

* Design a modern, professional, and visually striking user interface, catering to a diverse audience within large corporations, including executives, strategists, and environmental specialists.

* Construct an intuitive navigation system, allowing users to seamlessly access functionalities for informed decision-making and tracking progress towards net-zero emissions.

* The application is expected to be used on desktops first

* Incorporate our brand's colors, and visual elements into the design to maintain consistency throughout the application.

* Provide design assets and documentation, such as style guides, design specifications, and necessary assets (e.g., icons, illustrations) for our development team to implement the design. We use Figma and would appreciate delivery as figma files.

Please note that we also need more pages over time. The most important is to get the work bench page right. We will also need:
* a landing page where the users can select previous scenarios and see some high level data.
* A page with information on historical data per asset
* An analytics page
* User and system administration pages.
These pages are out of scope for this project, but they should be available in the navigation solution.

Please submit your initial design concepts, accompanied by a brief explanation of your approach and the rationale behind your design choices. We will offer feedback and collaborate with the chosen designer to refine the design, ensuring it meets our requirements and vision.

We are really hoping to see some elegant user interfaces. The functionality describe in the attachment is important, but the layout is not. Feel free to invent.

Attached files:

Target Market(s)

Energy intensive industries

Requirements
Must have
• Easy to navigate through the different data dimensions: Time, assets, mitigation measures, and advanced details under mitigation measures. The design in the attached files are just our working drafts. Creative alternatives are very welcome.
Nice to have
• Elegant layouts that differ from our working drafts.

```html
<!DOCTYPE html>
<html lang="en">
<head>
<meta charset="utf-8">
<title>KORVa Workbench – Design Concept</title>
<link href="https://fonts.googleapis.com/css2?family=Inter:wght@300;400;500;600;700&display=swap" rel="stylesheet">
<style>
:root{
  --navy:#0D4774;
  --blue:#105991;
  --teal:#438B93;
  --gold:#DDA01D;
  --sand:#EAC372;
  --violet:#976BB0;
  --coral:#E76D77;
  --sky:#8EC5F0;
  --sage:#5C9494;
  --mist:#E9EEF2;
  --stage:#049FFB;
  --panel:#F4F7FA;
  --hilite:#E3F0FC;
  --ok:#1AA46B;
  --muted:#9AA4AE;
  --ink:#1E2A36;
  --label:#6D7278;
}
*{box-sizing:border-box;margin:0;padding:0}
html,body{width:894px;height:1200px;overflow:hidden;background:#fff}
body{font-family:'Inter',sans-serif}
.page{position:relative;width:1652px;height:2218px;transform:scale(.54116);transform-origin:0 0;background:#fff}
.abs{position:absolute}
.band-top{left:0;top:0;width:1652px;height:1122px;background:var(--stage)}
.band-bottom{left:0;top:2012px;width:1652px;height:206px;background:var(--stage)}
.concept-title{left:137px;top:64px;font-size:40px;font-weight:400;color:#fff}

/* app frame */
.app{left:134px;top:178px;width:1384px;height:878px;background:var(--panel);overflow:hidden}
.topbar{left:0;top:0;width:1384px;height:54px;background:var(--navy)}
.brand{left:0;top:0;width:345px;height:54px;background:var(--blue);display:flex;align-items:center;justify-content:center;gap:8px;color:#fff;font-size:20px;font-weight:500;letter-spacing:3px}
.brand-dot{width:8px;height:8px;border-radius:50%;background:var(--sky)}
.nav-link{top:17px;font-size:16px;color:#fff}
.nav-link.current{font-weight:700}
.notice-dot{width:10px;height:10px;border-radius:50%;background:#F0453A}
.gear{left:1320px;top:12px;width:30px;height:30px;border-radius:50%;background:#2A5D86;display:flex;align-items:center;justify-content:center}

/* measures library */
.library{left:0;top:54px;width:345px;height:824px;background:#F2F6FA}
.panel-title{font-size:15px;font-weight:700;color:var(--navy);letter-spacing:.2px}
.search{display:flex;align-items:center;gap:14px;padding-left:18px;background:#E4EEF8;border-radius:19px;color:#7B8794;font-size:16px}
.filter-btn{border-radius:50%;background:#E4EEF8;display:flex;align-items:center;justify-content:center}
.group-head{left:0;width:345px;height:35px;background:var(--navy);color:#fff;font-size:14px;display:flex;align-items:center;padding-left:31px}
.group-head .applied{position:absolute;right:55px;font-size:12px;color:#BFD9F2}
.group-head .caret{position:absolute;left:302px;top:12px}
.measure-item{left:0;width:345px;height:32px;font-size:14px;color:#4D5965;display:flex;align-items:center;padding-left:46px}
.measure-item.on{background:var(--hilite);color:var(--ink)}
.measure-item .count{position:absolute;right:74px;font-size:12px;color:#8A96A2}
.measure-item.on .count{color:var(--ink)}
.tick-box{position:absolute;left:285px;top:10px;width:12px;height:12px;border-radius:2px;background:#D3DCE4}
.tick-box::after{content:"";position:absolute;left:3px;top:5px;width:6px;height:2px;background:#fff}
.measure-item.on .tick-box{background:#4E7089}

/* assets */
.assets{left:346px;top:54px;width:471px;height:568px;background:#F7F9FC}
.asset-row{left:376px;width:430px;height:20px;font-size:12px;color:var(--ink)}
.asset-row span{position:absolute;top:3px}
.status{position:absolute;width:13px;height:13px;border-radius:50%;background:var(--muted);display:flex;align-items:center;justify-content:center}
.status.ok{background:var(--ok)}
.settings-bar{left:346px;top:359px;width:471px;height:34px;background:#E4E8EE;font-size:12px;font-weight:700;color:var(--navy);display:flex;align-items:center;padding-left:30px}
.setting-row{left:376px;width:430px;height:20px;font-size:12px;color:#9AA2AA}
.setting-row.live{color:var(--ink)}
.setting-row .state{position:absolute;right:46px;top:2px}
.setting-row.live .state{color:var(--ok)}

/* simulation */
.simulation{left:817px;top:54px;width:567px;height:568px;background:#fff}
.view-icon{width:32px;height:32px;border-radius:50%;background:var(--mist);display:flex;align-items:center;justify-content:center}
.view-icon.current{background:var(--navy)}
.legend{font-size:12px;color:var(--navy);display:flex;align-items:center;gap:7px}
.legend i{width:8px;height:8px;border-radius:50%;display:block}
.axis-label{font-size:10px;color:var(--navy)}

/* timeline */
.timeline{left:346px;top:622px;width:1038px;height:256px;background:#EEF2F6}
.year{font-size:12px;color:var(--navy)}
.grid-line{width:1px;background:#D9E0E7}
.bar{height:35px;display:flex;align-items:center;padding-left:12px;color:#fff;font-size:14px}
.bar .modify{position:absolute;font-size:12px;display:flex;align-items:center;gap:9px}
.bar .modify b{width:11px;height:9px;border:1.5px solid #fff;border-radius:2px;display:block;position:relative}
.bar .modify b::after{content:"";position:absolute;left:2px;top:1.5px;width:3px;height:3px;background:#fff;border-radius:50%}
.gold{background:var(--gold)}
.violet{background:var(--violet)}
.sage{background:var(--sage)}
.view-toggle{height:35px;border-radius:18px;background:#fff;display:flex;overflow:hidden;box-shadow:0 2px 4px rgba(13,71,116,.15);font-size:12px}
.view-toggle div{display:flex;align-items:center;justify-content:center;gap:10px;color:var(--navy)}
.view-toggle .chosen{background:var(--navy);color:#fff}

/* style sheet */
.section-title{font-size:38px;font-weight:300;color:#555B62}
.icon-disc{width:56px;height:56px;border-radius:50%;display:flex;align-items:center;justify-content:center}
.icon-disc.soft{background:var(--mist)}
.icon-disc.solid{background:var(--navy)}
.swatch{width:42px;height:42px;border-radius:50%}
.swatch-label{font-size:16px;color:#7D848B;width:90px;text-align:center}
.closing{left:97px;font-size:23px;color:#fff}
.closing strong{font-weight:700}
</style>
</head>
<body>
<svg width="0" height="0" style="position:absolute">
  <defs>
    <symbol id="ico-trend" viewBox="0 0 24 24"><path d="M3 19V7l5 5 4-5 4 4 5-5v6l-5 4-4-4-4 5-5-3z" fill="currentColor"/><path d="M3 20h18" stroke="currentColor" stroke-width="2"/></symbol>
    <symbol id="ico-pie" viewBox="0 0 24 24"><path d="M11 2a10 10 0 1 0 0 20z" fill="currentColor"/><path d="M13 2a10 10 0 0 1 9 9h-9z M13 13h9a10 10 0 0 1-9 9z" fill="currentColor"/></symbol>
    <symbol id="ico-bars" viewBox="0 0 24 24"><rect x="4" y="11" width="4" height="9" fill="currentColor"/><rect x="10" y="5" width="4" height="15" fill="currentColor"/><rect x="16" y="14" width="4" height="6" fill="currentColor"/></symbol>
    <symbol id="ico-measures" viewBox="0 0 24 24"><path d="M4 3h16v9h-9v9H4z" fill="currentColor"/><rect x="7" y="6" width="3" height="3" fill="#fff"/><rect x="13" y="6" width="4" height="3" fill="#fff"/><rect x="7" y="12" width="3" height="5" fill="#fff"/></symbol>
    <symbol id="ico-asset" viewBox="0 0 24 24"><rect x="3" y="3" width="18" height="18" rx="4" fill="currentColor"/><rect x="7" y="7" width="10" height="2.5" fill="#fff"/></symbol>
    <symbol id="ico-check" viewBox="0 0 12 12"><path d="M3 6.2l2 2 4-4.4" fill="none" stroke="#fff" stroke-width="1.6"/></symbol>
    <symbol id="ico-caret-down" viewBox="0 0 12 8"><path d="M1 1h10L6 7z" fill="currentColor"/></symbol>
    <symbol id="ico-caret-left" viewBox="0 0 8 12"><path d="M7 1v10L1 6z" fill="currentColor"/></symbol>
  </defs>
</svg>

<main class="page">
  <div class="abs band-top"></div>
  <h1 class="abs concept-title">Design Concept pt 1:</h1>

  <section class="abs app">
    <header class="abs topbar">
      <div class="abs brand"><span class="brand-dot"></span>BRELMONT</div>
      <span class="abs nav-link" style="left:369px">Home</span>
      <span class="abs nav-link" style="left:443px">Assets</span>
      <span class="abs nav-link current" style="left:523px">Workbranch</span>
      <span class="abs nav-link" style="left:647px">Simulation</span>
      <span class="abs notice-dot" style="left:724px;top:16px"></span>
      <span class="abs nav-link" style="left:753px">Map</span>
      <span class="abs nav-link" style="left:1024px">Quick Actions</span>
      <svg class="abs" style="left:1137px;top:17px" width="16" height="20" viewBox="0 0 16 20"><path d="M10 1L2 12h6l-2 7 8-11H8z" fill="none" stroke="#8EC5F0" stroke-width="1.5"/></svg>
      <span class="abs nav-link" style="left:1208px">Mara Lind</span>
      <svg class="abs" style="left:1286px;top:24px;color:#fff" width="12" height="8"><use href="#ico-caret-down"/></svg>
      <div class="abs gear"><svg width="18" height="18" viewBox="0 0 24 24"><circle cx="12" cy="12" r="3.2" fill="none" stroke="#fff" stroke-width="2"/><path d="M12 2.5l2 2.6 3.2-.6.6 3.2 2.7 2-1.6 2.3 1.6 2.3-2.7 2-.6 3.2-3.2-.6-2 2.6-2-2.6-3.2.6-.6-3.2-2.7-2 1.6-2.3-1.6-2.3 2.7-2 .6-3.2 3.2.6z" fill="none" stroke="#fff" stroke-width="1.5"/></svg></div>
    </header>

    <aside class="abs library">
      <h2 class="abs panel-title" style="left:28px;top:13px">MEASURES LIBRARY</h2>
      <svg class="abs" style="left:312px;top:16px" width="18" height="18" viewBox="0 0 18 18"><rect x="1" y="1" width="16" height="16" rx="2" fill="none" stroke="#0D4774" stroke-width="2"/><rect x="3" y="3" width="6" height="12" fill="#0D4774"/></svg>
      <div class="abs search" style="left:48px;top:51px;width:222px;height:37px">
        <svg width="18" height="18" viewBox="0 0 18 18"><circle cx="7.5" cy="7.5" r="5.5" fill="none" stroke="#7B8794" stroke-width="2"/><path d="M11.5 11.5l5 5" stroke="#7B8794" stroke-width="2"/></svg>Search measures</div>
      <div class="abs filter-btn" style="left:280px;top:51px;width:36px;height:36px"><svg width="16" height="16" viewBox="0 0 16 16"><path d="M1 2h14l-5 6v6l-4-2V8z" fill="#8A96A2"/></svg></div>
    </aside>

    <div class="abs group-head" style="top:164px">Switch Energy Carrier<span class="applied">1 Applied</span><svg class="caret" width="12" height="8" style="color:#fff"><use href="#ico-caret-down"/></svg></div>
    <div class="abs measure-item" style="top:199px">Ammonium<span class="count">0/0</span><i class="tick-box"></i></div>
    <div class="abs measure-item on" style="top:231px">Biodiesel<span class="count">20/28</span><i class="tick-box"></i></div>
    <div class="abs measure-item" style="top:263px">Ethanol<span class="count">0/0</span><i class="tick-box"></i></div>
    <div class="abs measure-item" style="top:294px">Hydrogen<span class="count">0/0</span><i class="tick-box"></i></div>
    <div class="abs measure-item" style="top:326px">LNG<span class="count">0/0</span><i class="tick-box"></i></div>
    <div class="abs measure-item" style="top:358px">Methanol<span class="count">0/0</span><i class="tick-box"></i></div>
    <div class="abs measure-item" style="top:389px">Power from offshore wind<span class="count">0/0</span><i class="tick-box"></i></div>
    <div class="abs measure-item" style="top:421px">Power from shore<span class="count">0/0</span><i class="tick-box"></i></div>

    <div class="abs group-head" style="top:457px">Energy efficiency Measures<span class="applied">2 Applied</span><svg class="caret" width="12" height="8" style="color:#fff"><use href="#ico-caret-down"/></svg></div>
    <div class="abs measure-item" style="top:492px">Venting to flare<span class="count">0/0</span><i class="tick-box"></i></div>
    <div class="abs measure-item" style="top:524px">reduced water injection<span class="count">0/0</span><i class="tick-box"></i></div>
    <div class="abs measure-item on" style="top:556px">Reduced gaz injection<span class="count">18/18</span><i class="tick-box"></i></div>
    <div class="abs measure-item on" style="top:587px">Compressor replacement<span class="count">7/28</span><i class="tick-box"></i></div>
    <div class="abs measure-item" style="top:619px">Venting to production<span class="count">0/0</span><i class="tick-box"></i></div>
    <div class="abs measure-item" style="top:651px">Drilling Improvements<span class="count">0/0</span><i class="tick-box"></i></div>
    <div class="abs measure-item" style="top:683px">reduced water injection<span class="count">0/0</span><i class="tick-box"></i></div>

    <div class="abs group-head" style="top:719px">Logisticts<span class="applied">0 Applied</span><svg class="caret" width="8" height="12" style="color:#fff;top:11px"><use href="#ico-caret-left"/></svg></div>
    <div class="abs group-head" style="top:758px">End of pipe measures<span class="applied">0 Applied</span><svg class="caret" width="8" height="12" style="color:#fff;top:11px"><use href="#ico-caret-left"/></svg></div>
    <div class="abs group-head" style="top:797px">Carbon offsets<span class="applied">0 Applied</span><svg class="caret" width="8" height="12" style="color:#fff;top:11px"><use href="#ico-caret-left"/></svg></div>
    <div class="abs group-head" style="top:836px">Company Structure<span class="applied">0 Applied</span><svg class="caret" width="8" height="12" style="color:#fff;top:11px"><use href="#ico-caret-left"/></svg></div>

    <section class="abs assets">
      <h2 class="abs panel-title" style="left:18px;top:13px">ASSETS</h2>
    </section>
    <div class="abs asset-row" style="top:104px"><span style="left:0">Asset name</span><span style="left:120px">data</span><span style="left:200px">additionals</span><span style="left:315px">date</span><i class="status ok" style="left:397px;top:3px"><svg width="12" height="12"><use href="#ico-check"/></svg></i></div>
    <div class="abs asset-row" style="top:135px"><span style="left:0">Asset name</span><span style="left:120px">data</span><span style="left:200px">additionals</span><span style="left:315px">date</span><i class="status" style="left:397px;top:3px"><svg width="12" height="12"><use href="#ico-check"/></svg></i></div>
    <div class="abs asset-row" style="top:166px"><span style="left:0">Asset name</span><span style="left:120px">data</span><span style="left:200px">additionals</span><span style="left:315px">date</span><i class="status" style="left:397px;top:3px"><svg width="12" height="12"><use href="#ico-check"/></svg></i></div>
    <div class="abs asset-row" style="top:197px"><span style="left:0">Asset name</span><span style="left:120px">data</span><span style="left:200px">additionals</span><span style="left:315px">date</span><i class="status ok" style="left:397px;top:3px"><svg width="12" height="12"><use href="#ico-check"/></svg></i></div>
    <div class="abs asset-row" style="top:228px"><span style="left:0">Asset name</span><span style="left:120px">data</span><span style="left:200px">additionals</span><span style="left:315px">date</span><i class="status ok" style="left:397px;top:3px"><svg width="12" height="12"><use href="#ico-check"/></svg></i></div>
    <div class="abs asset-row" style="top:258px"><span style="left:0">Asset name</span><span style="left:120px">data</span><span style="left:200px">additionals</span><span style="left:315px">date</span><i class="status" style="left:397px;top:3px"><svg width="12" height="12"><use href="#ico-check"/></svg></i></div>

    <div class="abs settings-bar">Advanced Settings<svg class="abs" style="left:427px;top:13px;color:#0D4774" width="11" height="7"><use href="#ico-caret-down"/></svg></div>
    <div class="abs setting-row live" style="top:400px"><span class="abs" style="top:2px">Daily Monitoring</span><span class="state">Active</span><i class="status ok" style="left:397px;top:3px"><svg width="12" height="12"><use href="#ico-check"/></svg></i></div>
    <div class="abs setting-row" style="top:432px"><span class="abs" style="top:2px">Compression advaced configuration</span><span class="state">inactive</span><i class="status" style="left:397px;top:3px"><svg width="12" height="12"><use href="#ico-check"/></svg></i></div>
    <div class="abs setting-row" style="top:463px"><span class="abs" style="top:2px">Advanced Recast</span><span class="state">inactive</span><i class="status" style="left:397px;top:3px"><svg width="12" height="12"><use href="#ico-check"/></svg></i></div>
    <div class="abs setting-row" style="top:495px"><span class="abs" style="top:2px">Compressor failure safty</span><span class="state">inactive</span><i class="status" style="left:397px;top:3px"><svg width="12" height="12"><use href="#ico-check"/></svg></i></div>
    <div class="abs setting-row live" style="top:527px"><span class="abs" style="top:2px">Activated advanced setting</span><span class="state">Active</span><i class="status ok" style="left:397px;top:3px"><svg width="12" height="12"><use href="#ico-check"/></svg></i></div>
    <div class="abs setting-row" style="top:558px"><span class="abs" style="top:2px">This is an inactive one</span><span class="state">inactive</span><i class="status" style="left:397px;top:3px"><svg width="12" height="12"><use href="#ico-check"/></svg></i></div>

    <section class="abs simulation">
      <h2 class="abs panel-title" style="left:23px;top:19px">SIMULATION</h2>
      <div class="abs view-icon current" style="left:417px;top:13px;color:#fff"><svg width="18" height="18"><use href="#ico-trend"/></svg></div>
      <div class="abs view-icon" style="left:459px;top:13px;color:#0D4774"><svg width="18" height="18"><use href="#ico-pie"/></svg></div>
      <div class="abs view-icon" style="left:501px;top:13px;color:#0D4774"><svg width="18" height="18"><use href="#ico-bars"/></svg></div>
      <div class="abs legend" style="left:75px;top:71px"><i style="background:var(--violet)"></i>Accumulated Effect</div>
      <div class="abs legend" style="left:228px;top:71px"><i style="background:var(--gold)"></i>Second Strategy</div>
      <div class="abs legend" style="left:364px;top:71px"><i style="background:var(--coral)"></i>No Measures</div>
      <div class="abs legend" style="left:480px;top:71px"><i style="background:var(--sage)"></i>Goal</div>
      <svg class="abs" style="left:0;top:0" width="567" height="568" viewBox="951 232 567 568" role="img" aria-label="Emission forecast line chart, 2022 to 2027">
        <rect x="1092" y="330" width="64" height="414" fill="#F1F7FD"/>
        <rect x="1220" y="330" width="64" height="414" fill="#F1F7FD"/>
        <rect x="1348" y="330" width="64" height="414" fill="#F1F7FD"/>
        <line x1="1020" y1="744" x2="1488" y2="744" stroke="#C9D3DC"/>
        <g font-family="Inter, sans-serif" font-size="10" fill="#0D4774" text-anchor="middle">
          <text x="998" y="344">20</text><text x="998" y="445">15</text><text x="998" y="546">10</text><text x="995" y="647">5</text><text x="995" y="748">0</text>
          <text x="1089" y="765">2022</text><text x="1154" y="765">2023</text><text x="1219" y="765">2024</text><text x="1284" y="765">2025</text><text x="1350" y="765">2026</text><text x="1415" y="765">2027</text><text x="1479" y="765">2027</text>
        </g>
        <g fill="none" stroke-width="2.5" stroke-linecap="round">
          <path d="M1030 540 C1060 490 1080 465 1120 462 C1160 460 1190 455 1220 438 C1250 425 1280 420 1300 440 C1320 460 1350 455 1380 430 C1410 400 1440 395 1462 399" stroke="#E76D77"/>
          <path d="M1030 540 C1070 510 1100 480 1135 485 C1170 490 1190 540 1225 535 C1260 530 1300 500 1350 503 C1400 506 1430 515 1466 512" stroke="#DDA01D"/>
          <path d="M1030 540 C1060 520 1090 505 1110 515 C1150 535 1170 600 1200 598 C1240 595 1280 560 1330 557 C1380 555 1430 500 1466 484" stroke="#976BB0"/>
          <path d="M1030 540 C1070 515 1100 485 1130 500 C1170 520 1210 590 1240 610 C1270 625 1280 618 1300 630 C1330 650 1350 656 1380 656 C1420 660 1440 715 1472 716" stroke="#5C9494"/>
        </g>
      </svg>
    </section>

    <section class="abs timeline">
      <span class="abs year" style="left:20px;top:14px">2022</span>
      <span class="abs year" style="left:101px;top:14px">2023</span>
      <span class="abs year" style="left:182px;top:14px">2024</span>
      <span class="abs year" style="left:262px;top:14px">2025</span>
      <span class="abs year" style="left:343px;top:14px">2026</span>
      <span class="abs year" style="left:424px;top:14px">2027</span>
      <span class="abs year" style="left:503px;top:14px">2027</span>
      <span class="abs year" style="left:583px;top:14px">2029</span>
      <span class="abs year" style="left:664px;top:14px">2030</span>
      <span class="abs year" style="left:744px;top:14px">2031</span>
      <span class="abs year" style="left:824px;top:14px">2032</span>
      <span class="abs year" style="left:904px;top:14px">2033</span>
      <span class="abs year" style="left:986px;top:14px">2034</span>
      <i class="abs grid-line" style="left:34px;top:38px;height:218px"></i>
      <i class="abs grid-line" style="left:115px;top:38px;height:218px"></i>
      <i class="abs grid-line" style="left:196px;top:38px;height:218px"></i>
      <i class="abs grid-line" style="left:276px;top:38px;height:218px"></i>
      <i class="abs grid-line" style="left:357px;top:38px;height:218px"></i>
      <i class="abs grid-line" style="left:438px;top:38px;height:218px"></i>
      <i class="abs grid-line" style="left:517px;top:38px;height:218px"></i>
      <i class="abs grid-line" style="left:597px;top:38px;height:218px"></i>
      <i class="abs grid-line" style="left:678px;top:38px;height:218px"></i>
      <i class="abs grid-line" style="left:758px;top:38px;height:218px"></i>
      <i class="abs grid-line" style="left:838px;top:38px;height:218px"></i>
      <i class="abs grid-line" style="left:918px;top:38px;height:218px"></i>
      <i class="abs grid-line" style="left:1000px;top:38px;height:218px"></i>

      <div class="abs bar gold" style="left:33px;top:51px;width:365px">Compressor replacement<span class="modify" style="left:290px">Modify<b></b></span></div>
      <div class="abs bar gold" style="left:518px;top:51px;width:322px">Compressor replacement<span class="modify" style="left:245px">Modify<b></b></span></div>
      <div class="abs bar violet" style="left:116px;top:99px;width:321px;padding-left:23px">Biodiesel Enery Carrier<span class="modify" style="left:234px">Modify<b></b></span></div>
      <div class="abs bar sage" style="left:357px;top:147px;width:321px">Biodiesel Enery Carrier<span class="modify" style="left:245px">Modify<b></b></span></div>

      <div class="abs view-toggle" style="left:714px;top:199px;width:301px">
        <div style="width:160px">Measures View<svg width="14" height="14" style="color:#0D4774"><use href="#ico-measures"/></svg></div>
        <div class="chosen" style="width:141px;border-radius:18px">Assets View<svg width="14" height="14" style="color:#fff"><use href="#ico-asset"/></svg></div>
      </div>
    </section>
  </section>

  <!-- style sheet -->
  <h2 class="abs section-title" style="left:99px;top:1203px">Icons examples</h2>
  <h2 class="abs section-title" style="left:776px;top:1203px">Colors</h2>

  <div class="abs icon-disc soft" style="left:145px;top:1283px;color:#0D4774"><svg width="30" height="30"><use href="#ico-trend"/></svg></div>
  <div class="abs icon-disc soft" style="left:224px;top:1283px;color:#0D4774"><svg width="30" height="30"><use href="#ico-pie"/></svg></div>
  <div class="abs icon-disc soft" style="left:303px;top:1283px;color:#0D4774"><svg width="30" height="30"><use href="#ico-bars"/></svg></div>
  <div class="abs icon-disc soft" style="left:382px;top:1283px;color:#0D4774"><svg width="30" height="30"><use href="#ico-measures"/></svg></div>
  <div class="abs icon-disc soft" style="left:461px;top:1283px;color:#0D4774"><svg width="30" height="30"><use href="#ico-asset"/></svg></div>
  <div class="abs icon-disc solid" style="left:145px;top:1375px;color:#fff"><svg width="30" height="30"><use href="#ico-trend"/></svg></div>
  <div class="abs icon-disc solid" style="left:224px;top:1375px;color:#fff"><svg width="30" height="30"><use href="#ico-pie"/></svg></div>
  <div class="abs icon-disc solid" style="left:303px;top:1375px;color:#fff"><svg width="30" height="30"><use href="#ico-bars"/></svg></div>
  <div class="abs icon-disc solid" style="left:382px;top:1375px;color:#fff"><svg width="30" height="30" viewBox="0 0 24 24"><path d="M4 3h16v9h-9v9H4z" fill="#fff"/><rect x="7" y="6" width="3" height="3" fill="#0D4774"/><rect x="13" y="6" width="4" height="3" fill="#0D4774"/><rect x="7" y="12" width="3" height="5" fill="#0D4774"/></svg></div>
  <div class="abs icon-disc solid" style="left:461px;top:1375px"><svg width="30" height="30" viewBox="0 0 24 24"><rect x="3" y="3" width="18" height="18" rx="4" fill="#fff"/><rect x="7" y="7" width="10" height="2.5" fill="#0D4774"/></svg></div>

  <svg class="abs" style="left:157px;top:1483px" width="20" height="20" viewBox="0 0 20 20"><rect x="1" y="1" width="18" height="18" rx="2" fill="#B7C4CF"/><rect x="5" y="9" width="10" height="2" fill="#fff"/></svg>
  <svg class="abs" style="left:207px;top:1482px" width="22" height="22" viewBox="0 0 22 22"><circle cx="11" cy="11" r="10" fill="#5C9494"/><path d="M6.5 11.3l3 3 6-6.4" fill="none" stroke="#fff" stroke-width="2"/></svg>
  <svg class="abs" style="left:258px;top:1483px" width="20" height="20" viewBox="0 0 20 20"><rect x="1" y="1" width="18" height="18" rx="2" fill="#B9DAF5"/><rect x="5" y="9" width="10" height="2" fill="#fff"/></svg>
  <svg class="abs" style="left:308px;top:1482px" width="22" height="22" viewBox="0 0 22 22"><circle cx="11" cy="11" r="10" fill="#8EC5F0"/><path d="M6.5 11.3l3 3 6-6.4" fill="none" stroke="#fff" stroke-width="2"/></svg>

  <i class="abs swatch" style="left:821px;top:1283px;background:var(--navy)"></i>
  <i class="abs swatch" style="left:907px;top:1283px;background:var(--teal)"></i>
  <i class="abs swatch" style="left:994px;top:1283px;background:var(--gold)"></i>
  <i class="abs swatch" style="left:1082px;top:1283px;background:var(--sand)"></i>
  <i class="abs swatch" style="left:1169px;top:1283px;background:var(--violet)"></i>
  <i class="abs swatch" style="left:1254px;top:1283px;background:var(--coral)"></i>
  <span class="abs swatch-label" style="left:797px;top:1330px">#0D4774</span>
  <span class="abs swatch-label" style="left:883px;top:1330px">#438B93</span>
  <span class="abs swatch-label" style="left:970px;top:1330px">#DDA01D</span>
  <span class="abs swatch-label" style="left:1058px;top:1330px">#EAC372</span>
  <span class="abs swatch-label" style="left:1145px;top:1330px">#976BB0</span>
  <span class="abs swatch-label" style="left:1230px;top:1330px">#E76D77</span>
  <i class="abs swatch" style="left:818px;top:1378px;background:var(--blue)"></i>
  <i class="abs swatch" style="left:902px;top:1378px;background:var(--sky)"></i>
  <i class="abs swatch" style="left:989px;top:1378px;background:var(--sage)"></i>
  <i class="abs swatch" style="left:1075px;top:1378px;background:var(--mist)"></i>
  <span class="abs swatch-label" style="left:794px;top:1425px">#105991</span>
  <span class="abs swatch-label" style="left:878px;top:1425px">#8EC5F0</span>
  <span class="abs swatch-label" style="left:965px;top:1425px">#5C9494</span>
  <span class="abs swatch-label" style="left:1051px;top:1425px">#E9EEF2</span>

  <h2 class="abs section-title" style="left:99px;top:1622px">Assets examples</h2>

  <div class="abs bar violet" style="left:133px;top:1701px;width:320px;padding-left:23px">Biodiesel Enery Carrier<span class="modify" style="left:233px">Modify<b></b></span></div>
  <div class="abs bar gold" style="left:477px;top:1701px;width:364px">Compressor replacement<span class="modify" style="left:289px">Modify<b></b></span></div>
  <div class="abs group-head" style="left:865px;top:1701px;width:344px">Logisticts<span class="applied">0 Applied</span><svg class="caret" width="8" height="12" style="color:#fff;top:11px"><use href="#ico-caret-left"/></svg></div>
  <div class="abs measure-item on" style="left:1233px;top:1705px;width:344px;height:31px">Compressor replacement<span class="count">7/28</span><i class="tick-box" style="top:9px"></i></div>

  <div class="abs view-toggle" style="left:133px;top:1772px;width:300px">
    <div style="width:159px">Measures View<svg width="14" height="14" style="color:#0D4774"><use href="#ico-measures"/></svg></div>
    <div class="chosen" style="width:141px;border-radius:18px">Assets View<svg width="14" height="14" style="color:#fff"><use href="#ico-asset"/></svg></div>
  </div>
  <div class="abs search" style="left:477px;top:1772px;width:221px;height:37px">
    <svg width="18" height="18" viewBox="0 0 18 18"><circle cx="7.5" cy="7.5" r="5.5" fill="none" stroke="#7B8794" stroke-width="2"/><path d="M11.5 11.5l5 5" stroke="#7B8794" stroke-width="2"/></svg>Search measures</div>
  <div class="abs filter-btn" style="left:707px;top:1772px;width:38px;height:38px"><svg width="16" height="16" viewBox="0 0 16 16"><path d="M1 2h14l-5 6v6l-4-2V8z" fill="#8A96A2"/></svg></div>
  <div class="abs legend" style="left:788px;top:1785px"><i style="background:var(--violet)"></i>Accumulated Effect</div>

  <div class="abs" style="left:133px;top:1866px">
    <span class="abs year" style="left:0">2022</span><i class="abs grid-line" style="left:14px;top:24px;height:42px"></i>
    <span class="abs year" style="left:81px">2023</span><i class="abs grid-line" style="left:95px;top:24px;height:42px"></i>
    <span class="abs year" style="left:161px">2024</span><i class="abs grid-line" style="left:175px;top:24px;height:42px"></i>
    <span class="abs year" style="left:242px">2025</span><i class="abs grid-line" style="left:256px;top:24px;height:42px"></i>
    <span class="abs year" style="left:323px">2026</span><i class="abs grid-line" style="left:337px;top:24px;height:42px"></i>
    <span class="abs year" style="left:403px">2027</span><i class="abs grid-line" style="left:417px;top:24px;height:42px"></i>
    <span class="abs year" style="left:483px">2027</span><i class="abs grid-line" style="left:497px;top:24px;height:42px"></i>
    <span class="abs year" style="left:563px">2029</span><i class="abs grid-line" style="left:577px;top:24px;height:42px"></i>
    <span class="abs year" style="left:644px">2030</span><i class="abs grid-line" style="left:658px;top:24px;height:42px"></i>
    <span class="abs year" style="left:724px">2031</span><i class="abs grid-line" style="left:738px;top:24px;height:42px"></i>
    <span class="abs year" style="left:803px">2032</span><i class="abs grid-line" style="left:817px;top:24px;height:42px"></i>
    <span class="abs year" style="left:884px">2033</span><i class="abs grid-line" style="left:898px;top:24px;height:42px"></i>
    <span class="abs year" style="left:966px">2034</span><i class="abs grid-line" style="left:980px;top:24px;height:42px"></i>
  </div>

  <div class="abs band-bottom"></div>
  <p class="abs closing" style="top:2082px">Final Delivery will contain all the components, with any additional assets the you might need,</p>
  <p class="abs closing" style="top:2125px">please leave <strong>your feedback</strong> on this design, that way we can communicate on how to <strong>make the design better and make it fit your needs.</strong></p>
</main>
</body>
</html>
```